Business Card Design Project - Industrial Motor Rep

Create a business card that utilizes our existing logo found on our website: www.kestrelfluxsupply.com

We are a Industrial Distributor with a focus on electric motors. We represent several key brands which can be found on our web site. Our customer base includes Consultants, Large End Users (TQ, Lusk Chemical, Brevol) and original equipment manufacturers.

Industry/Entity Type

Business

Requirements
Must have
• Name, Title, Phone, Fax, Cell, Website, Mailing address

```html
<!DOCTYPE html>
<html lang="en">
<head>
<meta charset="utf-8">
<title>Kestrel Flux Supply – Business Card</title>
<link href="https://fonts.googleapis.com/css2?family=Share+Tech+Mono&display=swap" rel="stylesheet">
<style>
  :root {
    --backdrop: #e7e5e2;
    --card: #0c0c0c;
    --ink: #ffffff;
    --ink-soft: #e4e4e4;
  }
  * { margin: 0; padding: 0; box-sizing: border-box; }
  html, body {
    width: 1200px; height: 888px; overflow: hidden;
    background: var(--backdrop);
    font-family: "Share Tech Mono", monospace;
  }
  .canvas { position: relative; width: 1200px; height: 888px; }
  .card {
    position: absolute; left: 334px; width: 540px; height: 298px;
    background: var(--card);
    box-shadow: 0 3px 8px rgba(0,0,0,0.35);
  }
  .card--front { top: 112px; }
  .card--back { top: 434px; }

  .brand {
    position: absolute; left: 16px; top: 14px;
    display: flex; align-items: center; gap: 12px;
  }
  .brand__dot {
    width: 36px; height: 36px; border-radius: 50%;
    background: var(--ink);
  }
  .brand__name {
    color: var(--ink); font-size: 34px; line-height: 1;
    letter-spacing: 0.5px;
  }

  .contact {
    position: absolute; right: 26px; top: 128px;
    text-align: right; color: var(--ink-soft);
  }
  .contact__name { font-size: 17px; line-height: 20px; }
  .contact__title { font-size: 17px; line-height: 20px; margin-bottom: 12px; }
  .contact__line { font-size: 11.5px; line-height: 15px; }
  .contact__web { margin-top: 4px; }

  .back-mark {
    position: absolute; right: 34px; bottom: 50px;
    display: flex; align-items: center; gap: 12px;
  }
  .back-mark__dot {
    width: 36px; height: 36px; border-radius: 50%;
    background: var(--ink);
  }
  .back-mark__name {
    color: var(--ink); font-size: 44px; line-height: 1;
  }
</style>
</head>
<body>
<main class="canvas">
  <section class="card card--front" aria-label="Card front">
    <div class="brand">
      <span class="brand__dot"></span>
      <span class="brand__name">Kestrel Flux Supply</span>
    </div>
    <div class="contact">
      <p class="contact__name">Alan Reeve</p>
      <p class="contact__title">Special Job Title</p>
      <p class="contact__line">land line: 01632 960000</p>
      <p class="contact__line">mobile: 07700 900000</p>
      <p class="contact__line">fax: 01632 960000</p>
      <p class="contact__line">14 Forge Lane, Millbrook MB4 2QT</p>
      <p class="contact__line">sales@kestrelfluxsupply.com</p>
      <p class="contact__line contact__web">www.kestrelfluxsupply.com</p>
    </div>
  </section>

  <section class="card card--back" aria-label="Card back">
    <div class="back-mark">
      <span class="back-mark__dot"></span>
      <span class="back-mark__name">KFS</span>
    </div>
  </section>
</main>
</body>
</html>
```